Minimalist Modern Business Card Design, open to ideas, or cleaner version of provided files, but what logo & logo colors (with some black) as shown in files, and info for back shown in files as well.

```html
<!DOCTYPE html>
<html lang="en">
<head>
<meta charset="utf-8">
<title>Onward Depot Works – Business Card</title>
<link rel="stylesheet" href="https://fonts.googleapis.com/css2?family=Montserrat:wght@600&family=Work+Sans:wght@500;700&display=swap">
<style>
  :root {
    --backdrop: #d3d4d6;
    --navy: #25266a;
    --navy-deep: #202160;
    --ink: #161616;
    --paper: #ffffff;
  }
  * { margin: 0; padding: 0; box-sizing: border-box; }
  html, body {
    width: 900px;
    height: 1200px;
    overflow: hidden;
    background: var(--backdrop);
  }
  .canvas {
    position: relative;
    width: 900px;
    height: 1200px;
  }
  .card {
    position: absolute;
    left: 134px;
    width: 632px;
    height: 362px;
    overflow: hidden;
  }
  .card--front {
    top: 212px;
    background: linear-gradient(100deg, var(--navy-deep) 0%, var(--navy) 60%, #292a72 100%);
  }
  .card--back {
    top: 628px;
    background: var(--paper);
  }

  /* Wordmark: one colour, one weight */
  .wordmark {
    position: absolute;
    font-family: 'Montserrat', sans-serif;
    font-weight: 600;
    line-height: 1.02;
  }
  .wordmark span { display: block; }
  .card--front .wordmark {
    left: 260px;
    top: 138px;
    font-size: 40px;
    color: var(--paper);
  }
  .front-square {
    position: absolute;
    left: 168px;
    top: 146px;
    width: 68px;
    height: 68px;
    background: var(--paper);
  }
  .card--back .wordmark {
    left: 42px;
    top: 44px;
    font-size: 32px;
    color: var(--navy);
  }

  .back-block {
    position: absolute;
    left: 290px;
    top: 21px;
    width: 318px;
    height: 318px;
    background: var(--navy-deep);
  }

  .person {
    position: absolute;
    left: 43px;
    top: 192px;
    font-family: 'Work Sans', sans-serif;
  }
  .person__name {
    font-weight: 700;
    font-size: 23px;
    color: var(--navy);
    letter-spacing: 0.2px;
  }
  .person__title {
    font-weight: 500;
    font-size: 14px;
    color: var(--ink);
    margin-top: 2px;
    letter-spacing: 0.5px;
  }

  .contact {
    position: absolute;
    left: 43px;
    top: 268px;
    list-style: none;
    font-family: 'Work Sans', sans-serif;
    font-weight: 500;
    color: var(--ink);
  }
  .contact__item {
    display: flex;
    align-items: center;
    gap: 8px;
    height: 18px;
    margin-bottom: 8px;
    font-size: 14px;
  }
  .contact__item--phone { letter-spacing: 3px; }
  .contact__item--email { letter-spacing: 0.4px; }
  .contact__icon { width: 15px; height: 15px; flex: none; }
</style>
</head>
<body>
<main class="canvas">

  <section class="card card--front" aria-label="Card front">
    <div class="front-square" aria-hidden="true"></div>
    <h1 class="wordmark"><span>Onward</span><span>Depot Works</span></h1>
  </section>

  <section class="card card--back" aria-label="Card back">
    <h2 class="wordmark"><span>Onward</span><span>Depot Works</span></h2>

    <div class="person">
      <p class="person__name">MY NAME</p>
      <p class="person__title">President</p>
    </div>

    <ul class="contact">
      <li class="contact__item contact__item--phone">
        <svg class="contact__icon" viewBox="0 0 16 16" aria-hidden="true">
          <rect x="3.5" y="0.5" width="9" height="15" rx="1.5" fill="var(--navy)"/>
          <rect x="5" y="2.5" width="6" height="9.5" fill="#fff"/>
          <circle cx="8" cy="13.8" r="0.8" fill="#fff"/>
        </svg>
        123-123-4567
      </li>
      <li class="contact__item contact__item--email">
        <svg class="contact__icon" viewBox="0 0 16 16" aria-hidden="true">
          <rect x="0.5" y="3" width="15" height="10" fill="var(--navy)"/>
          <path d="M0.5 3.5 L8 9 L15.5 3.5" fill="none" stroke="#fff" stroke-width="1.3"/>
        </svg>
        xxxxxxx@xxxxxx.com
      </li>
    </ul>

    <div class="back-block" aria-hidden="true"></div>
  </section>

</main>
</body>
</html>
```